Property Services Company Needs a Brochure Design

Looking for a new brochure design for an existing property services company.

We provide a range of property services from, market research, real estate brokerage, valuation and appraisal, property development and other real estate consulting services.

We would like a fresh modern brochure design with good graphics and features. Our colours are white, blue and orange.

The design should communicate, attention to detail, superior service delivery and distinction in results.
Updates

I would like the brochure to be roughly about 20 pages.

Containing the following,

1) An introduction
2) Contents Page
2) What we do
3) Our Services
4) Agency & Brokerage
5) Real Estate Consulting
6) Market Research
7) Appraisal & Valuation
8) Project Management
9) Property Development

I would also like icons to represent items 4,5,6,7,8 & 9, they should be represented vertically on each of the pages from the contents page and highlighted individually on the pages that they represent.. i.e. on appraisal & valuation page, all six icons will be arranged vertically and the appraisal and valuations icon will be highlighted.

I will also like to have images that depict the services on the various pages.

I have some pages I think will flow which I will upload shortly.

Industry/Entity Type

Real Estate

Font styles to use
Serif

Colors
f78f20
0455a3

```html
<!DOCTYPE html>
<html lang="en">
<head>
<meta charset="utf-8">
<title>Marlowe Property Services – Brochure</title>
<link rel="stylesheet" href="https://fonts.googleapis.com/css2?family=Open+Sans:wght@400;600;700&family=Arimo:wght@400&display=swap">
<style>
  :root {
    --stage: #2b2b2d;
    --slate: #2a333f;
    --slate-light: #344050;
    --blue: #0455a3;
    --blue-deep: #0a3577;
    --orange: #f78f20;
    --orange-deep: #d9761a;
    --paper: #ffffff;
    --paper-shade: #e4e4e6;
    --ink: #2a2a2a;
    --navy: #1f2a5c;
  }
  * { margin: 0; padding: 0; box-sizing: border-box; }
  html, body { width: 1200px; height: 900px; overflow: hidden; background: var(--stage); }
  .canvas { position: relative; width: 1200px; height: 900px; font-family: "Open Sans", sans-serif; }
  .page { position: absolute; overflow: hidden; }
  .page > svg { position: absolute; inset: 0; width: 100%; height: 100%; }

  .back-cover { left: 95px; top: 92px; width: 505px; height: 358px; }
  .contact-title { position: absolute; left: 52px; top: 236px; font-family: "Arimo", sans-serif; font-size: 15px; font-weight: 400; color: #e8ecf2; }
  .contact-list { position: absolute; left: 89px; top: 278px; list-style: none; font-family: "Arimo", sans-serif; font-size: 10px; line-height: 12px; color: #e8ecf2; }

  .front-cover { left: 635px; top: 95px; width: 515px; height: 355px; }
  .brand { position: absolute; left: 310px; top: 34px; display: flex; align-items: center; gap: 8px; }
  .brand-mark { width: 14px; height: 14px; background: var(--orange); }
  .brand-name { font-size: 29px; font-weight: 600; color: var(--navy); line-height: 1; }
  .brand-tagline { position: absolute; left: 364px; top: 70px; font-size: 9.5px; font-weight: 600; color: var(--navy); }

  .spread { left: 110px; top: 475px; width: 1005px; height: 355px; }
  .section-label { position: absolute; font-size: 10px; font-weight: 700; color: #111; letter-spacing: 0.2px; }
  .intro-label { left: 52px; top: 18px; }
  .content-label { left: 912px; top: 11px; }
  .intro-body { position: absolute; left: 48px; top: 60px; font-size: 9.2px; line-height: 11.5px; color: var(--ink); white-space: nowrap; }
  .intro-body p { margin-bottom: 11.5px; }

  .contents-list { position: absolute; right: 27px; top: 58px; list-style: none; text-align: right; }
  .contents-list li { height: 28px; font-size: 12px; font-weight: 700; color: #fff6ea; line-height: 20px; }
</style>
</head>
<body>
<main class="canvas">

  <section class="page back-cover">
    <svg viewBox="0 0 505 358" preserveAspectRatio="none">
      <defs>
        <linearGradient id="slateFade" x1="0" y1="0" x2="0" y2="1">
          <stop offset="0" stop-color="var(--slate)"/>
          <stop offset="1" stop-color="var(--slate-light)"/>
        </linearGradient>
        <linearGradient id="bluePattern" x1="0" y1="0" x2="1" y2="1">
          <stop offset="0" stop-color="var(--blue-deep)"/>
          <stop offset="1" stop-color="var(--blue)"/>
        </linearGradient>
      </defs>
      <rect width="505" height="358" fill="url(#slateFade)"/>
      <polygon points="505,172 505,358 335,358" fill="url(#bluePattern)" role="img" aria-label="Blue honeycomb texture panel"/>
    </svg>
    <h2 class="contact-title">Contact information</h2>
    <ul class="contact-list">
      <li>Adress</li>
      <li>Phone</li>
      <li>email adress</li>
      <li>web adress</li>
    </ul>
  </section>

  <section class="page front-cover">
    <svg viewBox="0 0 515 355" preserveAspectRatio="none">
      <defs>
        <linearGradient id="paperFade" x1="1" y1="0" x2="0" y2="1">
          <stop offset="0" stop-color="var(--paper-shade)"/>
          <stop offset="0.5" stop-color="var(--paper)"/>
          <stop offset="1" stop-color="var(--paper-shade)"/>
        </linearGradient>
        <linearGradient id="bluePatternFront" x1="0" y1="0" x2="1" y2="1">
          <stop offset="0" stop-color="var(--blue)"/>
          <stop offset="1" stop-color="var(--blue-deep)"/>
        </linearGradient>
      </defs>
      <rect width="515" height="355" fill="var(--slate)"/>
      <polygon points="0,165 115,42 345,225 250,355 0,355" fill="url(#bluePatternFront)" role="img" aria-label="Blue honeycomb texture panel"/>
      <polygon points="250,355 345,225 475,355" fill="var(--slate)"/>
      <polygon points="98,0 515,0 515,340" fill="url(#paperFade)"/>
      <polygon points="75,0 98,0 515,340 515,355 510,355" fill="var(--orange)"/>
    </svg>
    <div class="brand">
      <span class="brand-mark"></span>
      <span class="brand-name">Marlowe</span>
    </div>
    <span class="brand-tagline">Property Services</span>
  </section>

  <section class="page spread">
    <svg viewBox="0 0 1005 355" preserveAspectRatio="none">
      <defs>
        <linearGradient id="pageFade" x1="0" y1="0" x2="1" y2="0">
          <stop offset="0" stop-color="#f4f4f5"/>
          <stop offset="0.6" stop-color="var(--paper)"/>
          <stop offset="1" stop-color="var(--paper-shade)"/>
        </linearGradient>
        <linearGradient id="bluePatternSpread" x1="0" y1="0" x2="1" y2="1">
          <stop offset="0" stop-color="var(--blue)"/>
          <stop offset="1" stop-color="var(--blue-deep)"/>
        </linearGradient>
        <linearGradient id="bannerFade" x1="0" y1="0" x2="1" y2="0">
          <stop offset="0" stop-color="var(--orange-deep)"/>
          <stop offset="1" stop-color="var(--orange)"/>
        </linearGradient>
        <linearGradient id="photoTones" x1="0" y1="0" x2="1" y2="1">
          <stop offset="0" stop-color="#d9d6d0"/>
          <stop offset="0.55" stop-color="#6e6f78"/>
          <stop offset="1" stop-color="#2c2f3c"/>
        </linearGradient>
      </defs>
      <rect width="500" height="355" fill="url(#pageFade)"/>
      <rect width="25" height="355" fill="url(#bluePatternSpread)" role="img" aria-label="Blue honeycomb texture strip"/>
      <polygon points="300,355 500,148 500,355" fill="url(#bluePatternSpread)" role="img" aria-label="Blue honeycomb texture panel"/>
      <polygon points="287,355 497,138 505,146 300,355" fill="var(--orange)"/>

      <rect x="500" width="505" height="355" fill="url(#bluePatternSpread)" role="img" aria-label="Blue honeycomb texture background"/>
      <polygon points="550,0 1005,0 1005,355 932,355" fill="url(#pageFade)"/>
      <polygon points="538,0 550,0 932,355 920,355" fill="var(--orange)"/>
      <polygon points="600,50 1005,50 1005,275 835,275" fill="url(#bannerFade)"/>
      <g stroke="#fff6ea" stroke-width="0.8" opacity="0.7">
        <line x1="640" y1="80" x2="1005" y2="80"/>
        <line x1="670" y1="108" x2="1005" y2="108"/>
        <line x1="700" y1="136" x2="1005" y2="136"/>
        <line x1="730" y1="164" x2="1005" y2="164"/>
        <line x1="760" y1="192" x2="1005" y2="192"/>
        <line x1="790" y1="220" x2="1005" y2="220"/>
        <line x1="820" y1="248" x2="1005" y2="248"/>
      </g>
      <rect x="505" y="110" width="313" height="237" fill="url(#photoTones)" role="img" aria-label="Photo of a smiling businessman in a suit reading a document"/>
    </svg>

    <h2 class="section-label intro-label">INTRODUCTION</h2>
    <div class="intro-body">
      <p>MARLOWE was incorporated in 1984 as an interior design and property development<br>company. Over the years we have expanded our service with a foundation based on core<br>strengths, unrivalled local expertise, network and knowledge combined with strategic<br>partnerships.</p>
      <p>Marlowe offers a comprehensive range of services&nbsp; on a local, regional, national and interna-<br>tional basis to tenants, owners, and investors within the residential and commercial property<br>market.</p>
      <p>Our clients depend on our ability to draw on years of experience in the local market, our<br>professionals know their communities and the property market inside and out,<br>and provide knowledgeable, creative solutions to all their real estate needs.</p>
      <p>We currently provide services to corporations, financial institutions,<br>government agencies, public sector entities, developers and investors.<br>Our knowledge, expertise, experience and technological resources<br>allow us to be a superior service provider.</p>
    </div>

    <h2 class="section-label content-label">CONTENT</h2>
    <ul class="contents-list">
      <li>What we do</li>
      <li>Our Services</li>
      <li>Agency &amp; Brokerage</li>
      <li>Real Estate Consulting</li>
      <li>Market Research</li>
      <li>Appraisal &amp; Valuation</li>
      <li>Project Management</li>
      <li>Property Development</li>
    </ul>
  </section>

</main>
</body>
</html>
```